Exciting New Health Brand. Needs packaging design

We need a label and packaging design for a US based colloidal Silver water product due to launch shortly.
we like the vibe and feel of this: https://www.shopvarlo.example/Pure-Brightwell-Dropper-Top-Regal-Tonic/dp/K48TRW2MPL/ref=sr_1_1_sspa?ie=UTF8&qid=1520284298&sr=8-1-spons&keywords=regal+tonic+colloidal+tonic&psc=1 though would need to make it look different

Target Market(s)

people who like natural health, and alternative health such as yoga, reiki etc

Industry/Entity Type

Health And Wellness

Font styles to use
Other font styles liked:
• open minded

Colors

Designer to choose colors to be used in the design.

Requirements
Must have
• Vibrant feel.Brand name is fernwell vitals
Nice to have
• quite open minded
Should not have
• mustn't have cheap animated look

```html
<!DOCTYPE html>
<html lang="en">
<head>
<meta charset="utf-8">
<title>Fernwell Vitals – Bio-Active Label</title>
<link rel="stylesheet" href="https://fonts.googleapis.com/css2?family=Marcellus&family=Tinos&display=swap">
<style>
  :root {
    --page: #f4f4f4;
    --label-dark: #1c1c1c;
    --label-mid: #2e2e2e;
    --frame: #8a8a8a;
    --ink-light: #f2f2f2;
    --ink-soft: #d8d8d8;
    --band-light: #d9d9d9;
    --band-mid: #a9a9a9;
    --band-dark: #6f6f6f;
    --band-ink: #1a1a1a;
  }
  * { margin: 0; padding: 0; box-sizing: border-box; }
  html, body { width: 1200px; height: 1200px; overflow: hidden; }
  body {
    background: var(--page);
    display: flex;
    align-items: center;
    justify-content: center;
  }
  .label {
    position: relative;
    width: 720px;
    height: 1060px;
    background: linear-gradient(135deg, var(--label-mid) 0%, var(--label-dark) 45%, var(--label-mid) 70%, var(--label-dark) 100%);
    overflow: hidden;
  }
  .label__frame {
    position: absolute;
    inset: 24px;
    border: 2px solid var(--frame);
    pointer-events: none;
  }
  .brand-panel {
    position: absolute;
    left: 60px;
    right: 60px;
    top: 50px;
    height: 380px;
    border-radius: 22px;
    background: linear-gradient(180deg, rgba(255,255,255,0.07) 0%, rgba(255,255,255,0.02) 100%);
    border: 1px solid rgba(255,255,255,0.06);
  }
  .brand-name {
    position: absolute;
    left: 0;
    right: 0;
    top: 150px;
    text-align: center;
    font-family: "Marcellus", serif;
    font-size: 94px;
    line-height: 128px;
    color: var(--ink-light);
    letter-spacing: 1px;
  }
  .variant-band {
    position: absolute;
    left: 26px;
    right: 26px;
    top: 550px;
    height: 130px;
    background: linear-gradient(90deg, var(--band-dark) 0%, var(--band-light) 30%, var(--band-mid) 60%, var(--band-light) 80%, var(--band-dark) 100%);
    display: flex;
    align-items: center;
    justify-content: center;
    font-family: "Marcellus", serif;
    font-size: 80px;
    color: var(--band-ink);
  }
  .product-type {
    position: absolute;
    left: 0;
    right: 0;
    top: 852px;
    text-align: center;
    font-family: "Marcellus", serif;
    font-size: 56px;
    color: var(--ink-soft);
  }
  .volume {
    position: absolute;
    left: 208px;
    top: 986px;
    font-family: "Tinos", serif;
    font-size: 24px;
    color: var(--ink-soft);
  }
</style>
</head>
<body>
  <main class="label">
    <div class="brand-panel"></div>
    <h1 class="brand-name">FERNWELL<br>VITALS</h1>
    <div class="variant-band">BIO - ACTIVE</div>
    <p class="product-type">Dietary Suppement</p>
    <p class="volume">8 fl. oz. 236 ml</p>
    <div class="label__frame"></div>
  </main>
</body>
</html>
```